New lease of life for a tired Country Pub menu, QLD

I need to refresh my menus with updated prices. The menus need to be A4 (the menus are laminated and handed out over the bar. I'd like to include our logo. I will upload our existing menus as well as the new prices. The design should be humble yet stylish if that's ok, please

Target Market(s)

Locals, travellers and workers

Industry/Entity Type

Hospitality, Quintessential Country pub

Font styles to use
Sans Serif

Colors

Designer to choose colors to be used in the design.

Requirements
Must have
• as we run different menus on different nights
Nice to have
• our logo

```html
<!DOCTYPE html>
<html lang="en">
<head>
<meta charset="utf-8">
<title>Hotel Bramley – Dinner Menu</title>
<link rel="stylesheet" href="https://fonts.googleapis.com/css2?family=Cormorant+Garamond:wght@500;600&family=Great+Vibes&family=Raleway:wght@400;500;700&display=swap">
<style>
  :root {
    --ink: #1a1816;
    --cream: #e3d4a9;
    --gold: #a8792f;
    --paper: #ffffff;
  }
  * { box-sizing: border-box; margin: 0; padding: 0; }
  html, body { width: 1200px; height: 826px; overflow: hidden; background: var(--paper); }
  body { position: relative; font-family: "Raleway", sans-serif; color: var(--cream); }

  .menu-page { position: absolute; top: 0; width: 584px; height: 826px; background: var(--ink); overflow: hidden; }
  .menu-page--mains { left: 0; }
  .menu-page--extras { left: 616px; }
  .page-frame { position: absolute; inset: 0; }

  .venue-name {
    position: absolute; left: 0; width: 584px; top: 62px; text-align: center;
    font-family: "Raleway", sans-serif; font-weight: 700; font-size: 18px; line-height: 21px;
    letter-spacing: 0.5px; color: var(--cream);
  }
  .menu-title {
    position: absolute; left: 0; width: 584px; top: 128px; text-align: center;
    font-family: "Cormorant Garamond", serif; font-weight: 600; font-size: 64px; line-height: 1;
    letter-spacing: 2px; color: var(--cream);
  }
  .section-title {
    position: absolute; font-family: "Great Vibes", cursive; font-weight: 400;
    font-size: 44px; line-height: 1; color: var(--gold); text-align: center; white-space: nowrap;
  }

  .item-list { position: absolute; list-style: none; }
  .item { display: flex; align-items: baseline; white-space: nowrap; }
  .item-leader { flex: 1; border-bottom: 1.5px dotted var(--cream); margin: 0 3px; transform: translateY(-3px); min-width: 8px; }
  .item-leader--short { flex: 0 0 22px; }

  .starter-list { top: 287px; width: 176px; font-size: 11.5px; line-height: 16px; text-transform: uppercase; }
  .starter-list .item-price, .side-list .item-price, .kids-list .item-price {
    font-family: "Cormorant Garamond", serif; font-weight: 600; font-size: 11.5px;
  }

  .main-list { left: 71px; width: 432px; font-size: 13.5px; line-height: 16px; }
  .main-list .item-price { font-size: 12.5px; font-weight: 500; }

  .side-list { width: 215px; font-size: 11px; line-height: 23.5px; text-transform: uppercase; }
  .kids-list { left: 53px; width: 215px; font-size: 11px; line-height: 14px; text-transform: uppercase; }
  .kids-list .item { margin-bottom: 9.5px; }
  .kids-list .item-indent { padding-left: 11px; }

  .dessert-note {
    position: absolute; left: 300px; width: 240px; top: 532px; text-align: center;
    font-family: "Great Vibes", cursive; font-size: 20px; line-height: 24px; color: var(--cream);
  }

  .drinks { position: absolute; top: 675px; left: 53px; display: flex; }
  .drinks-group { width: 126px; list-style: none; font-size: 9.5px; line-height: 15.6px; }
  .drinks-heading { font-size: 11.5px; line-height: 16px; font-weight: 500; margin-bottom: 1px; }
</style>
</head>
<body>

<section class="menu-page menu-page--mains" aria-label="Dinner menu, mains side">
  <svg class="page-frame" width="584" height="826" viewBox="0 0 584 826" aria-hidden="true">
    <rect x="20" y="16" width="546" height="793" fill="none" stroke="var(--cream)" stroke-width="1.5"/>
    <rect x="26" y="22" width="534" height="781" fill="none" stroke="var(--cream)" stroke-width="1"/>
  </svg>
  <svg class="page-frame" width="584" height="826" viewBox="0 0 584 826">
    <rect role="img" aria-label="Corner scroll flourish" x="14" y="10" width="34" height="34" fill="var(--cream)" opacity="0.22"/>
    <rect role="img" aria-label="Corner scroll flourish" x="538" y="10" width="34" height="34" fill="var(--cream)" opacity="0.22"/>
    <rect role="img" aria-label="Corner scroll flourish" x="14" y="781" width="34" height="34" fill="var(--cream)" opacity="0.22"/>
    <rect role="img" aria-label="Corner scroll flourish" x="538" y="781" width="34" height="34" fill="var(--cream)" opacity="0.22"/>
  </svg>

  <p class="venue-name">HOTEL<br>BRAMLEY</p>
  <h1 class="menu-title">DINNER MENU</h1>

  <h2 class="section-title" style="left:0;width:584px;top:225px;">Garlic Bread Starters</h2>
  <ul class="item-list starter-list" style="left:71px;">
    <li class="item"><span>Regular</span><span class="item-leader"></span><span class="item-price">$10.50</span></li>
    <li class="item"><span>Cheesy Garlic</span><span class="item-leader"></span><span class="item-price">$12.00</span></li>
  </ul>
  <ul class="item-list starter-list" style="left:327px;">
    <li class="item"><span>Cheesy Sweet Chili</span><span class="item-leader"></span><span class="item-price">$12.50</span></li>
    <li class="item"><span>Loaded</span><span class="item-leader"></span><span class="item-price">$15.00</span></li>
  </ul>

  <h2 class="section-title" style="left:0;width:584px;top:349px;">Main Course</h2>
  <ul class="item-list main-list" style="top:403px;">
    <li class="item"><span>T-Bone Steak</span><span class="item-leader"></span><span class="item-price">$41.99</span></li>
    <li class="item"><span>Rump Steak</span><span class="item-leader"></span><span class="item-price">$40.99</span></li>
    <li class="item"><span>Crumbed Steak</span><span class="item-leader"></span><span class="item-price">$28.99</span></li>
  </ul>
  <ul class="item-list main-list" style="top:465px;">
    <li class="item"><span>Lamb Rosemary Filo</span><span class="item-leader"></span><span class="item-price">$24.99</span></li>
    <li class="item"><span>Lamb Shank and Mash</span><span class="item-leader"></span><span class="item-price">$32.00</span></li>
    <li class="item"><span>Lamb Loin Chops</span><span class="item-leader"></span><span class="item-price">$35.00</span></li>
  </ul>
  <ul class="item-list main-list" style="top:530px;">
    <li class="item"><span>Pork Chop(s)</span><span class="item-leader"></span><span class="item-price">(1) $29.00</span><span class="item-leader item-leader--short"></span><span class="item-price">(2) $32.99</span></li>
  </ul>
  <ul class="item-list main-list" style="top:574px;">
    <li class="item"><span>Chicken and Mushroom Filo</span><span class="item-leader"></span><span class="item-price">$24.99</span></li>
    <li class="item"><span>Crumbed Chicken Thigh</span><span class="item-leader"></span><span class="item-price">$27.99</span></li>
  </ul>
  <ul class="item-list main-list" style="top:619px;">
    <li class="item"><span>Bangers and Mash</span><span class="item-leader"></span><span class="item-price">$23.00</span></li>
    <li class="item"><span>Rissoles and Mash</span><span class="item-leader"></span><span class="item-price">$23.00</span></li>
  </ul>
  <ul class="item-list main-list" style="top:665px;">
    <li class="item"><span>Roasted Veggie Scroll</span><span class="item-leader"></span><span class="item-price">$24.99</span></li>
  </ul>
  <ul class="item-list main-list" style="top:695px;">
    <li class="item"><span>Beer Battered Flathead (Main)</span><span class="item-leader"></span><span class="item-price">$27.99</span></li>
    <li class="item"><span>Barramundi Panko</span><span class="item-leader"></span><span class="item-price">$27.99</span></li>
    <li class="item"><span>Calamari Panko Crumbed</span><span class="item-leader"></span><span class="item-price">$27.99</span></li>
    <li class="item"><span>Seafood Basket</span><span class="item-leader"></span><span class="item-price">$27.99</span></li>
  </ul>
</section>

<section class="menu-page menu-page--extras" aria-label="Dinner menu, sides and drinks side">
  <svg class="page-frame" width="584" height="826" viewBox="0 0 584 826" aria-hidden="true">
    <path d="M20 413 V16 H566 V413 M26 413 V22 H560 V413" fill="none" stroke="var(--cream)" stroke-width="1.5"/>
    <path d="M20 419 V809 H566 V419 M26 419 V803 H560 V419" fill="none" stroke="var(--gold)" stroke-width="1.5"/>
  </svg>
  <svg class="page-frame" width="584" height="826" viewBox="0 0 584 826">
    <rect role="img" aria-label="Corner scroll flourish" x="14" y="10" width="34" height="34" fill="var(--cream)" opacity="0.22"/>
    <rect role="img" aria-label="Corner scroll flourish" x="538" y="10" width="34" height="34" fill="var(--cream)" opacity="0.22"/>
    <rect role="img" aria-label="Corner scroll flourish" x="14" y="781" width="34" height="34" fill="var(--gold)" opacity="0.35"/>
    <rect role="img" aria-label="Corner scroll flourish" x="538" y="781" width="34" height="34" fill="var(--gold)" opacity="0.35"/>
  </svg>

  <p class="venue-name">HOTEL<br>BRAMLEY</p>
  <h1 class="menu-title">DINNER MENU</h1>

  <h2 class="section-title" style="left:63px;width:200px;top:222px;">Sides</h2>
  <ul class="item-list side-list" style="left:53px;top:282px;">
    <li class="item"><span>Small Bowl of Chips</span><span class="item-leader"></span><span class="item-price">$9.50</span></li>
    <li class="item"><span>Large Bowl of Chips</span><span class="item-leader"></span><span class="item-price">$12.50</span></li>
    <li class="item"><span>Mash Potatoes</span><span class="item-leader"></span><span class="item-price">$4.99</span></li>
    <li class="item"><span>Side Salad</span><span class="item-leader"></span><span class="item-price">$10.00</span></li>
  </ul>

  <h2 class="section-title" style="left:321px;width:200px;top:222px;">Extras</h2>
  <ul class="item-list side-list" style="left:310px;top:282px;">
    <li class="item"><span>Diane Sauce</span><span class="item-leader"></span><span class="item-price">$9.50</span></li>
    <li class="item"><span>Gravy</span><span class="item-leader"></span><span class="item-price">$12.50</span></li>
    <li class="item"><span>Mushroom Sauce</span><span class="item-leader"></span><span class="item-price">$4.99</span></li>
    <li class="item"><span>Pepper Sauce</span><span class="item-leader"></span><span class="item-price">$10.00</span></li>
    <li class="item"><span>Aioli</span><span class="item-leader"></span><span class="item-price">$9.50</span></li>
    <li class="item"><span>Mayonnaise</span><span class="item-leader"></span><span class="item-price">$12.50</span></li>
    <li class="item"><span>Tartar</span><span class="item-leader"></span><span class="item-price">$4.99</span></li>
  </ul>

  <h2 class="section-title" style="left:40px;width:246px;top:405px;">Kids Menu</h2>
  <ul class="item-list kids-list" style="top:464px;">
    <li class="item" style="margin-bottom:0;"><span>Beer Battered</span></li>
    <li class="item"><span class="item-indent">Flat Bread (Kids)</span><span class="item-leader"></span><span class="item-price">$9.50</span></li>
    <li class="item"><span>Nuggets &amp; Chips</span><span class="item-leader"></span><span class="item-price">$12.50</span></li>
    <li class="item"><span>Calamari &amp; Chips</span><span class="item-leader"></span><span class="item-price">$4.99</span></li>
    <li class="item" style="margin-bottom:0;"><span>Hawaiian Pizza</span></li>
    <li class="item"><span class="item-indent">and Chips</span><span class="item-leader"></span><span class="item-price">$10.00</span></li>
  </ul>

  <h2 class="section-title" style="left:321px;width:200px;top:475px;">Desserts</h2>
  <p class="dessert-note">Ask your server about today’s<br>delicious selection</p>

  <h2 class="section-title" style="left:192px;width:220px;top:622px;">Beverages</h2>
  <div class="drinks">
    <ul class="drinks-group">
      <li class="drinks-heading">SOFT DRINKS</li>
      <li>Cola, Diet Cola,</li>
      <li>Lemonade, Root Beer,</li>
      <li>Orange Soda</li>
    </ul>
    <ul class="drinks-group">
      <li class="drinks-heading">JUICES</li>
      <li>Orange</li>
      <li>Apples</li>
      <li>Cranberry</li>
    </ul>
    <ul class="drinks-group">
      <li class="drinks-heading">Coffee &amp; Tea</li>
      <li>Regular</li>
      <li>Decaf</li>
      <li>Orange Pekoe</li>
      <li>Earl Grey</li>
      <li>English Breakfast</li>
    </ul>
    <ul class="drinks-group">
      <li class="drinks-heading">BEER &amp; WINE</li>
      <li>Gold Lager</li>
      <li>Northern Pale</li>
      <li>Ridge Ale</li>
      <li>House Red</li>
      <li>House White</li>
    </ul>
  </div>
</section>

</body>
</html>
```